Website for online Real Estate School

I need to have three drop boxes which are really the main item on our web site. These tabs will need to be front and center “call to action”. Our sole goal on our site is to sell real estate courses which will be connected to these drop boxes. So please make this “call to action” section “clean” and the main emphasis on the page. We will fill in the items in the drop box so please ensure we have that ability.

 Get your license
 Post-Licensing
 Continuing Education

You could use the statement; “The Path to Your Future”

I’d like the design to be one where you keep scrolling down instead of having 5 or 6 tabs up top with different pages.

As you scan down I’d like to include the graphics and text as shown on one of the attachments. I copied this from another site so I’d ask you provide another logo. I already amended the text

People enter the real estate field with diverse educational backgrounds and overall goals. Some enter to only work part time to supplement their current income, and others full time. One person may enter the commercial market space and another residential. There is a wide range of directions you can take and the sky is truly the limit. Whichever path you take, your chances of success are directly related to your level of preparation and commitment. This is one career that really rewards self-motivated individuals.

 Careers - Career fields include residential and commercial real estate agents, brokers, mortgage brokers, property managers and independent investors. Many of these careers are held by independent people who have a strong entrepreneurial spirit. As you enter the real estate business in general its not unlikely you will be in it for life in one way or another. In our opinion it truly is the best path to wealth.
 Salary - According to the Norland Office of Trade Figures, real estate brokers earned a median annual wage of $56,860 and the highest 10 percent earned more than $166,940. An agent’s income is only limited to how much work you want to put into your business. We highly suggest you consider a few of our partners offers below as they can truly help you work smarter, not harder.
 Degrees - A real estate license will provide all you will need to enter the real estate business. Each state has requirements that you complete “Continuing Education” every other year. There are several other courses that will provide you with certifications which demonstrate your sophistication therefore we recommend you continue your pursuit of education and we certainly hope you do so with us.

We highly recommend you consider a few of out strategic partners as their services are a tremendous advantage to real estate professionals.

Here we will have 6-8 banners from companies that we will be affiliates with.

At this point I’m not interested in providing an address nor phone number for contact.

Our web site domain is; www.MeridelPropertyAcademy.com

I have a number of graphics that I will upload the .ai file. Feel free to improve as you see fit.

I included a few copies of our competition. PLEASE, do some basic research.... in short, we are a national school that sells real estate licensing education for your initial license and also continuing education. We sooooooo want to be better than our competitors. Please help us achieve this. zintro real estate license and real estate continuing education and look at competitors... Please. That way you truly know what we need to beat.

This is my 40th ish project on craft hive and appreciate everyone's work which is why I always come back.

We will be EXTREMELY RESPONSIVE AND LOG ON 5-10X A DAY TO COMMENT ON DESIGNS. PLEASE ONLY MESSAGE US ON THE DESIGN ITSELF VS VIA THE MAIL SYSTEM AS ITS EASIER FOR US. THANKS!!!

Reason: We have extended this project for 5 days as we think 2 days was a bit ambitious. We look forward to your designs

18-40 year old consumers. Aspiring and existing real estate agents and brokers

Real Estate

Coded - Design and coding required

1 page

• your choice

• clean site... please review the competition by searching on zintro; real estate continuing education and real estate license
• just clean site. nice and simple and be sure to have the call to action sections as the emphasis

```html
<!DOCTYPE html>
<html lang="en">
<head>
<meta charset="utf-8">
<title>Meridel Property Academy</title>
<link href="https://fonts.googleapis.com/css2?family=Cinzel:wght@400;600&family=Lato:wght@400;700&display=swap" rel="stylesheet">
<style>
:root{
  --navy:#0e3a78;
  --navy-dark:#0a2d5e;
  --orange:#f7941d;
  --orange-dark:#e07f0c;
  --ink:#3a3a3a;
  --muted:#6d6d6d;
  --light:#f1f1f1;
  --white:#ffffff;
}
*{margin:0;padding:0;box-sizing:border-box}
html,body{width:1200px;height:3291px;overflow:hidden;background:var(--white)}
body{position:relative;font-family:'Lato',Arial,sans-serif;color:var(--ink)}
.abs{position:absolute}

/* header */
.site-header{left:0;top:0;width:1200px;height:120px;background:var(--white)}
.brand{left:96px;top:22px;display:flex;align-items:center;gap:10px}
.brand-mark{width:18px;height:18px;background:var(--orange)}
.brand-name{font-family:'Lato',sans-serif;font-weight:700;font-size:20px;color:var(--navy);line-height:1.1;width:150px}
.top-email{right:96px;top:14px;display:flex;align-items:center;gap:12px;font-size:15px;color:var(--ink)}
.top-email .ico{width:32px;height:32px;border-radius:50%;background:var(--orange);display:flex;align-items:center;justify-content:center}
.main-nav{right:96px;top:72px;display:flex;gap:24px;font-family:'Cinzel',serif;font-size:16px;color:var(--ink)}
.main-nav a{color:inherit;text-decoration:none}
.main-nav a.active{color:var(--orange);border-bottom:2px solid var(--orange);padding-bottom:4px}

/* hero */
.hero{left:0;top:120px;width:1200px;height:532px;background:linear-gradient(120deg,#d9d6d2 0%,#eeeceb 40%,#cfd0d3 70%,#b9aea6 100%)}
.hero-arrow{top:226px;width:38px;height:38px;background:#2a2a2a;display:flex;align-items:center;justify-content:center}
.cta-panel{left:99px;top:341px;width:811px;height:99px;background:rgba(14,58,120,.85);padding:14px 24px}
.cta-title{font-family:'Cinzel',serif;color:var(--white);font-size:22px;letter-spacing:.5px}
.cta-options{display:flex;align-items:center;gap:34px;margin-top:16px;color:var(--white);font-size:18px}
.cta-option{display:flex;align-items:center;gap:10px}
.radio{width:16px;height:16px;border-radius:50%;background:var(--white);border:3px solid var(--white)}
.radio.on{background:var(--orange)}
.btn-start{margin-left:auto;background:var(--orange);color:var(--white);font-size:16px;font-weight:700;border-radius:18px;padding:6px 8px 6px 16px;display:flex;align-items:center;gap:10px}
.btn-start .dot{width:24px;height:24px;border-radius:50%;background:var(--white);display:flex;align-items:center;justify-content:center}
.hero-band{left:0;top:455px;width:1200px;height:77px;background:rgba(30,30,30,.78);text-align:center;font-family:'Cinzel',serif;font-size:32px;color:var(--white);line-height:77px}
.hero-band span{color:var(--orange)}

/* intro */
.intro{left:100px;top:690px;width:1000px;text-align:center;font-family:'Cinzel',serif;font-size:24px;line-height:34px;color:var(--ink)}

/* split sections */
.split{left:0;width:1200px}
.split .half{position:absolute;top:0;width:600px;height:100%;padding:38px 160px 0 99px}
.split .left{left:0;background:var(--navy)}
.split .right{left:600px;background:var(--orange);padding-left:160px;padding-right:99px}
.split h2{font-family:'Cinzel',serif;font-weight:400;font-size:28px;color:var(--white);padding-bottom:16px;border-bottom:1px solid rgba(255,255,255,.35);margin-bottom:20px}
.split p{font-size:15px;line-height:24px;color:var(--white)}
.split .more{color:var(--orange)}
.split .right .more{color:var(--navy)}
.emblem{position:absolute;left:480px;width:240px;height:240px;border-radius:50%;background:var(--white);display:flex;align-items:center;justify-content:center;text-align:center;font-weight:700;font-size:22px;color:var(--navy);line-height:1.2;padding:30px}

/* why choose */
.why{left:0;top:1141px;width:1200px;height:724px;background:linear-gradient(#ffffff,#eeeeee)}
.section-title{position:absolute;left:0;width:1200px;text-align:center;font-family:'Cinzel',serif;font-size:32px;color:var(--navy)}
.section-title span{color:var(--orange)}
.title-rule{position:absolute;left:520px;width:160px;height:1px;background:#c8c8c8}
.chart-label{position:absolute;width:180px;margin-left:-90px;text-align:center;color:var(--white);font-size:16px;font-weight:700;line-height:20px}
.exp-box{left:127px;top:246px;width:202px;height:44px;background:var(--white);border:1px solid #ccc;font-size:18px;color:var(--navy);display:flex;align-items:center;justify-content:center}

/* testimonials */
.testimonials{left:0;top:2234px;width:1200px;height:460px;background:var(--white)}
.testi{position:absolute;top:170px;width:318px;text-align:center}
.avatar{width:84px;height:84px;border-radius:50%;margin:0 auto;border:4px solid var(--orange);background:linear-gradient(#d8c6b6,#a98c76)}
.testi-name{margin-top:18px;font-weight:700;font-size:14px;color:var(--ink)}
.testi-handle{font-size:13px;color:var(--navy);margin-top:4px}
.quote-box{margin-top:24px;height:104px;border:1px solid #ddd;border-bottom:3px solid var(--navy);text-align:left;padding:14px 18px;font-size:14px;line-height:21px;color:var(--muted);position:relative}
.quote-box:before{content:"";position:absolute;top:-9px;left:40px;width:16px;height:16px;background:var(--white);border-left:1px solid #ddd;border-top:1px solid #ddd;transform:rotate(45deg)}
.quote-box b{color:#bbb;font-size:20px}

/* affiliates */
.affiliates{left:0;top:2694px;width:1200px;height:272px;background:linear-gradient(#f2f2f2,#e3e3e3)}
.aff-row{position:absolute;left:99px;top:154px;display:flex;gap:26px}
.aff{width:148px;height:70px;background:var(--white);border:1px solid #ddd;display:flex;align-items:center;justify-content:center;font-size:18px;font-weight:700;color:#4a4a4a}
.aff-arrow{position:absolute;top:170px}

/* footer */
.site-footer{left:0;top:2966px;width:1200px;height:277px;background:var(--navy)}
.f-col{position:absolute;top:30px}
.f-col h3{font-family:'Lato',sans-serif;font-weight:400;font-size:22px;color:var(--white);margin-bottom:22px}
.f-col h3 span{color:var(--orange)}
.links{display:flex;gap:50px;font-size:14px;color:var(--white)}
.links ul{list-style:none}
.links li{margin-bottom:12px}
.links li:before{content:"•";color:var(--orange);margin-right:8px}
.contact{font-size:14px;color:var(--white);line-height:20px}
.contact .row{display:flex;align-items:center;gap:8px;margin-top:10px}
.field{width:259px;height:34px;background:var(--white);margin-bottom:8px;font-size:12px;color:#999;padding:9px 10px}
.field.tall{height:38px}
.submit{width:120px;height:34px;background:var(--orange);color:var(--white);font-size:15px;display:flex;align-items:center;justify-content:center}
.social{font-size:13px;color:var(--white);font-weight:700}
.social .row{display:flex;align-items:center;gap:12px;margin-bottom:12px}
.social .c{width:30px;height:30px;border-radius:50%}
.copyright{left:0;top:3243px;width:1200px;height:48px;background:var(--navy-dark);color:var(--white);font-size:14px;text-align:center;line-height:48px;border-top:1px solid rgba(255,255,255,.15)}
</style>
</head>
<body>

<header class="site-header abs">
  <div class="brand abs"><span class="brand-mark"></span><span class="brand-name">Meridel Property Academy</span></div>
  <div class="top-email abs">
    <span class="ico"><svg width="16" height="12" viewBox="0 0 16 12"><rect x="0.5" y="0.5" width="15" height="11" fill="none" stroke="#fff"/><path d="M1 1l7 6 7-6" fill="none" stroke="#fff"/></svg></span>
    hello@meridelpropertyacademy.com
  </div>
  <nav class="main-nav abs">
    <a class="active">Home</a><a>About</a><a>Courses</a><a>Careers</a><a>Earning Expections</a><a>Licenses</a><a>Our Affiliates</a><a>Contact</a>
  </nav>
</header>

<section class="hero abs" role="img" aria-label="Photo of an instructor presenting at a flip chart to a group of real estate students">
  <div class="hero-arrow abs" style="left:8px"><svg width="12" height="16"><path d="M10 2L3 8l7 6" fill="none" stroke="#fff" stroke-width="2.5"/></svg></div>
  <div class="hero-arrow abs" style="right:8px"><svg width="12" height="16"><path d="M2 2l7 6-7 6" fill="none" stroke="#fff" stroke-width="2.5"/></svg></div>
  <div class="cta-panel abs">
    <div class="cta-title">Lorem ipsum dolor sit amet consectetuer adipi dolor almet</div>
    <div class="cta-options">
      <span class="cta-option"><span class="radio on"></span>Get your license</span>
      <span class="cta-option"><span class="radio"></span>Post-Licensing</span>
      <span class="cta-option"><span class="radio"></span>Continuing Education</span>
      <span class="btn-start">GET STARTED <span class="dot"><svg width="10" height="10"><path d="M2 1l5 4-5 4" fill="none" stroke="#f7941d" stroke-width="2"/></svg></span></span>
    </div>
  </div>
  <div class="hero-band abs">The Path to <span>Your Future</span></div>
</section>

<p class="intro abs">We are a national school that sells real estate licensing education for your initial license and also continuing education</p>

<section class="split abs" style="top:797px;height:344px">
  <div class="half left">
    <h2>Who We Are</h2>
    <p>People enter the real estate field with diverse educational backgrounds and overall goals. Some enter to only work part time to supplement their current income, and others full time. One person may enter the commercial market space and another residential. There is a wide range of directions you can take and the sky is truly the limit. Whichever path you take, your...<span class="more">[+]</span></p>
  </div>
  <div class="half right">
    <h2>What We Do</h2>
    <p>Career fields include residential and commercial real estate agents, brokers, mortgage brokers, property managers and independent investors. Many of these careers are held by independent people who have a strong entrepreneurial spirit. As you enter the real estate business in general its not unlikely you will be in it for life in one way or another. In our opinion it truly... <span class="more">[+]</span></p>
  </div>
  <div class="emblem" style="top:52px">Meridel Property Academy</div>
</section>

<section class="why abs">
  <h2 class="section-title" style="top:52px">Why <span>Choose Us?</span></h2>
  <div class="title-rule" style="top:104px"></div>
  <svg class="abs" style="left:0;top:0" width="1200" height="724" viewBox="0 0 1200 724">
    <polygon points="208,575 355,385 498,480 737,236 875,385 1022,280 1097,215 1097,625 208,625" fill="#0e3a78"/>
    <polyline points="160,612 355,362 498,456 737,213 875,362 1022,258 1090,190" fill="none" stroke="#f7941d" stroke-width="24" stroke-linejoin="miter"/>
    <g stroke="#fff" stroke-width="2">
      <line x1="355" y1="362" x2="355" y2="460"/>
      <line x1="498" y1="456" x2="498" y2="545"/>
      <line x1="737" y1="213" x2="737" y2="398"/>
      <line x1="875" y1="362" x2="875" y2="515"/>
      <line x1="1022" y1="258" x2="1022" y2="450"/>
    </g>
    <g fill="#fff">
      <circle cx="355" cy="460" r="5"/><circle cx="498" cy="545" r="5"/><circle cx="737" cy="398" r="5"/><circle cx="875" cy="515" r="5"/><circle cx="1022" cy="450" r="5"/>
    </g>
    <g fill="#fff" stroke="#f7941d" stroke-width="7">
      <circle cx="355" cy="362" r="17"/><circle cx="498" cy="456" r="17"/><circle cx="737" cy="213" r="17"/><circle cx="875" cy="362" r="17"/><circle cx="1022" cy="258" r="17"/>
    </g>
  </svg>
  <div class="exp-box abs">Year of Experience</div>
  <div class="abs" role="img" aria-label="Cartoon of a student working on a laptop at a desk" style="left:66px;top:351px;width:175px;height:264px;background:linear-gradient(#f3d9a8,#b98a52);border-radius:8px"></div>
  <div class="abs" role="img" aria-label="Illustration of a rocket launching upward" style="left:1042px;top:121px;width:143px;height:131px;background:linear-gradient(135deg,#fbb25a,#f7941d);border-radius:60px 8px 60px 8px"></div>
  <div class="chart-label" style="left:355px;top:474px">State-Approved<br>Courses</div>
  <div class="chart-label" style="left:498px;top:557px">Convenient 100%<br>Online Courses</div>
  <div class="chart-label" style="left:737px;top:410px">Meets State License<br>Requirements</div>
  <div class="chart-label" style="left:875px;top:528px">Quick, Easy, and<br>Affordable</div>
  <div class="chart-label" style="left:1022px;top:464px">Train on<br>Your Schedule</div>
</section>

<section class="split abs" style="top:1865px;height:369px">
  <div class="half left">
    <h2>Earning Expections</h2>
    <p>According to the Norland Office of Trade Figures, real estate brokers earned a median annual wage of $56,860 and the highest 10 percent earned more than $166,940. An agent’s income is only limited to how much work you want to put into your business. We highly suggest you consider a few of our partners offers below as they can truly help you work smarter, not harder.</p>
  </div>
  <div class="half right">
    <h2>Licenses</h2>
    <p>A real estate license will provide all you will need to enter the real estate business. Each state has requirements that you complete “Continuing Education” every other year. There are several other courses that will provide you with certifications which demonstrate your sophistication therefore we recommend you continue your pursuit of education and we certainly hope you do so with us.</p>
  </div>
  <div class="emblem" style="top:64px">Meridel Property Academy</div>
</section>

<section class="testimonials abs">
  <h2 class="section-title" style="top:44px">Client <span>Testimonials</span></h2>
  <div class="title-rule" style="top:94px"></div>
  <div class="testi" style="left:99px">
    <div class="avatar" role="img" aria-label="Portrait photo of the client"></div>
    <div class="testi-name">Miss Jana Delmore</div><div class="testi-handle">@jdelmore</div>
    <div class="quote-box"><b>“</b> Ut wisi enim ad minim veniam, quisl mor nostrni exerci tation ullamcorper suskcipit no lobortis norl nislk ut aliquip.</div>
  </div>
  <div class="testi" style="left:441px">
    <div class="avatar" role="img" aria-label="Portrait photo of the client"></div>
    <div class="testi-name">Miss Rona Gartley</div><div class="testi-handle">@rgartley</div>
    <div class="quote-box"><b>“</b> Ut wisi enim ad minim veniam, quisl mor nostrni exerci tation ullamcorper suskcipit no lobortis norl nislk ut aliquip.</div>
  </div>
  <div class="testi" style="left:783px">
    <div class="avatar" role="img" aria-label="Portrait photo of the client"></div>
    <div class="testi-name">Miss Sela Hlanu</div><div class="testi-handle">@shlanu</div>
    <div class="quote-box"><b>“</b> Ut wisi enim ad minim veniam, quisl mor nostrni exerci tation ullamcorper suskcipit no lobortis norl nislk ut aliquip.</div>
  </div>
</section>

<section class="affiliates abs">
  <h2 class="section-title" style="top:46px">Our <span>Affiliates</span></h2>
  <div class="title-rule" style="top:96px"></div>
  <svg class="aff-arrow" style="left:56px" width="20" height="40"><path d="M17 2L3 20l14 18" fill="none" stroke="#bbb" stroke-width="2"/></svg>
  <div class="aff-row">
    <div class="aff">Quillmere</div><div class="aff">Nestavo</div><div class="aff">Brivander</div><div class="aff">Tarvello</div><div class="aff">Ostrimo</div><div class="aff">Lumenfay</div>
  </div>
  <svg class="aff-arrow" style="left:1122px" width="20" height="40"><path d="M3 2l14 18L3 38" fill="none" stroke="#bbb" stroke-width="2"/></svg>
</section>

<footer class="site-footer abs">
  <div class="f-col" style="left:99px">
    <h3>Quick <span>Links</span></h3>
    <div class="links">
      <ul><li>Home</li><li>About</li><li>Courses</li><li>Careers</li><li>Salary</li></ul>
      <ul><li>Degrees</li><li>Our Affiliates</li><li>Contact</li></ul>
    </div>
  </div>
  <div class="f-col contact" style="left:366px">
    <h3>Contact <span>Details</span></h3>
    <div>Meridel Property Academy</div>
    <div>48 Alder Row, Suite 12,<br>Norland Heights 20417</div>
    <div class="row"><svg width="14" height="14" viewBox="0 0 14 14"><path d="M3 1l3 3-2 2c1 2 2 3 4 4l2-2 3 3-2 2C6 13 1 8 1 3z" fill="#f7941d"/></svg>(555) 014 2290</div>
    <div class="row"><svg width="14" height="14" viewBox="0 0 14 14"><path d="M3 1l3 3-2 2c1 2 2 3 4 4l2-2 3 3-2 2C6 13 1 8 1 3z" fill="#f7941d"/></svg>(555) 014 2290</div>
    <div class="row"><svg width="14" height="10" viewBox="0 0 14 10"><rect width="14" height="10" fill="#f7941d"/><path d="M0 0l7 5 7-5" fill="none" stroke="#0e3a78"/></svg>hello@meridelpropertyacademy.com</div>
  </div>
  <div class="f-col" style="left:658px">
    <h3>Quick <span>Inquiry</span></h3>
    <div class="field">Name</div>
    <div class="field">Email</div>
    <div class="field tall">Message</div>
    <div class="submit">Submit</div>
  </div>
  <div class="f-col social" style="left:987px">
    <h3>Follow <span>Us</span></h3>
    <div class="row"><span class="c" style="background:#3b5a9a"></span>HALVERLY</div>
    <div class="row"><span class="c" style="background:#2aa3d8"></span>KESTWING</div>
    <div class="row"><span class="c" style="background:#1c6fa8"></span>LINVORA</div>
    <div class="row"><span class="c" style="background:#d0382b"></span>ZINTRO +</div>
  </div>
</footer>
<div class="copyright abs">Copyright © 2016 Meridel Property Academy. All Rights Reserved.</div>

</body>
</html>
```